Brindle Fixings Company needs a label design

We need a label for our packaging. Our products are fasteners, for example, bolts, screws and nuts. We would like to see designs which is remarkable and impressive. Enclosed is our logo and packaging.

Label I want is for both external carton and internal small box or hang plastic blister. Must not contain our company logo, but use similar color mix to logo which is black and red. Pls design another new logo in the label. And leave some blank area for printing product info. Update sample label in my brief. It's a sample for your reference, pls dont use the same color and design.

It Company

```html
<!DOCTYPE html>
<html lang="en">
<head>
<meta charset="utf-8">
<title>Brindle Fixings – Fastener Label</title>
<link rel="stylesheet" href="https://fonts.googleapis.com/css2?family=Arimo:wght@400;700&display=swap">
<style>
  :root {
    --ink: #0d0d0d;
    --charcoal: #1c1c1e;
    --graphite: #2e2e31;
    --red: #d3141c;
    --red-deep: #8e0b10;
    --band-pale: #f1e4e4;
    --white: #ffffff;
    --steel-light: #c9ced8;
    --steel-dark: #5d6678;
  }
  * { margin: 0; padding: 0; box-sizing: border-box; }
  html, body { width: 1200px; height: 775px; overflow: hidden; background: var(--ink); }
  .label {
    position: relative;
    width: 1200px;
    height: 775px;
    overflow: hidden;
    background: linear-gradient(135deg, var(--graphite) 0%, var(--charcoal) 50%, var(--ink) 100%);
    font-family: "Arimo", Arial, sans-serif;
  }
  .wave { position: absolute; left: 0; top: 0; width: 1200px; height: 775px; }
  .brand {
    position: absolute;
    display: flex;
    align-items: center;
    gap: 12px;
    color: var(--white);
    font-weight: 700;
    text-transform: uppercase;
    line-height: 1.08;
  }
  .brand-mark { background: var(--red); flex: none; }
  .brand--top { left: 24px; top: 26px; font-size: 32px; letter-spacing: 2px; }
  .brand--top .brand-mark { width: 44px; height: 44px; }
  .brand--corner { right: 16px; top: 622px; font-size: 23px; letter-spacing: 1.5px; }
  .brand--corner .brand-mark { width: 30px; height: 30px; }
  .product-art {
    position: absolute;
    left: 22px;
    top: 358px;
    width: 392px;
    height: 322px;
    border-radius: 22px;
    background: radial-gradient(ellipse at 40% 45%, var(--steel-light) 0%, var(--steel-dark) 75%);
  }
  .tagline-bar {
    position: absolute;
    left: 0;
    bottom: 0;
    width: 1200px;
    height: 78px;
    background: var(--red);
    display: flex;
    align-items: center;
    justify-content: center;
  }
  .tagline {
    color: var(--white);
    font-size: 62px;
    font-weight: 400;
    letter-spacing: 1px;
    line-height: 1;
    white-space: nowrap;
  }
</style>
</head>
<body>
  <main class="label">
    <svg class="wave" viewBox="0 0 1200 775" preserveAspectRatio="none" aria-hidden="true">
      <path d="M0,110 C150,150 240,260 420,255 C640,245 820,90 1200,92 L1200,132 C860,140 660,300 430,305 C230,310 120,250 0,210 Z" fill="var(--band-pale)" opacity="0.9"/>
      <path d="M0,210 C120,250 230,310 430,305 C660,300 860,140 1200,132" fill="none" stroke="var(--white)" stroke-width="8"/>
      <path d="M0,278 C140,320 280,345 470,320 C700,285 900,185 1200,160 L1200,198 C910,222 710,320 480,352 C280,378 140,360 0,318 Z" fill="var(--red)"/>
      <path d="M0,336 C140,378 290,392 490,368 C720,335 920,238 1200,212" fill="none" stroke="var(--red-deep)" stroke-width="4"/>
    </svg>

    <div class="brand brand--top">
      <span class="brand-mark"></span>
      <span>Brindle<br>Fixings</span>
    </div>

    <div class="product-art" role="img" aria-label="Illustration of steel fasteners: screws, bolts, nuts and a washer"></div>

    <div class="brand brand--corner">
      <span class="brand-mark"></span>
      <span>Brindle<br>Fixings</span>
    </div>

    <footer class="tagline-bar">
      <p class="tagline">Manufacturer &amp; Exporting of Fasteners</p>
    </footer>
  </main>
</body>
</html>
```